【 概要 】 弊社vidmoraチャンネルの動画サムネイル案。1枚です。 サムネイルタイトルは以下の通りです。 文字のニュアンスは変更も可です! 【来週の相場は高確率で火曜日がXデーの理由】 弊社のVIDMORAは下記の通りです。ご参考下さい。 https://www.vidmora-sample.com/channel/UCkTrwQbNeHs4Lpa8_Dx2gZM?view_as=subscriber 【 依頼詳細 】 VIDMORAでアップする動画のサムネイル画像をお願いしたいです。 ロゴのイメージはお任せします。クリック率が増えれば何でもOK! VIDMORAを実際にアップロードしてクリック率が高ければ来週も継続させてほしいです。 【 デザインイメージ 】 ・ターゲット層:投資家・投資が気になってくる40代以降 ・雰囲気:若者向けのイメージではないです。 ・参考デザイン:弊社のvidmoraを見て頂くとつかめます。 【 契約金額(税抜) 】 2千円 その他ご質問等ありましたら、気軽にお問い合わせください。 ご応募をお待ちしております! |
| https://www.vidmora-sample.com/channel/UCkTrwQbNeHs4Lpa8_Dx2gZM?view_as=subscriber | ||
お世話になっております
楓林投資顧問で御座います。
採用ボタンを発見致しました。
採用の理由としましては、
視聴者に目を引くサムネイルのデザインと文字色と配色のバランスでした。
以上となります。
今後ともよろしくお願いいたします。
皆様ご提案ありがとうございます!
たくさんのサムネイル案、どれも素晴らしいクオリティーでした!

```html
<!DOCTYPE html>
<html lang="ja">
<head>
<meta charset="utf-8">
<title>来週の相場は高確率で火曜日がXデーの理由</title>
<link rel="stylesheet" href="https://fonts.googleapis.com/css2?family=Noto+Sans+JP:wght@900&display=swap">
<style>
  :root {
    --board-dark: #0b0f12;
    --board-mid: #1c2a2a;
    --ticker-green: #1f8a4a;
    --ticker-red: #8a1f1f;
    --headline-yellow: #fff200;
    --headline-green: #39d42a;
    --label-red: #e60012;
    --ink-black: #000000;
    --paper-white: #ffffff;
    --suit-navy: #1a2440;
  }
  * { margin: 0; padding: 0; box-sizing: border-box; }
  html, body { width: 1200px; height: 676px; overflow: hidden; background: var(--board-dark); }
  .thumbnail {
    position: relative;
    width: 1200px;
    height: 676px;
    overflow: hidden;
    font-family: "Noto Sans JP", sans-serif;
    font-weight: 900;
  }
  .market-board {
    position: absolute; inset: 0;
    background:
      radial-gradient(ellipse at 20% 40%, rgba(31,138,74,0.35), transparent 55%),
      radial-gradient(ellipse at 75% 30%, rgba(138,31,31,0.35), transparent 50%),
      linear-gradient(120deg, var(--board-mid), var(--board-dark) 60%);
  }
  .speaker-photo {
    position: absolute;
    left: 700px; top: 70px;
    width: 500px; height: 606px;
    background: linear-gradient(180deg, #3a3f4a 0%, var(--suit-navy) 55%, #10162a 100%);
    border-radius: 220px 220px 0 0;
    box-shadow: 0 0 40px rgba(255,255,255,0.35);
  }
  .topic-label {
    position: absolute;
    left: 0; top: 0;
    padding: 4px 22px 8px 14px;
    background: var(--label-red);
    color: var(--paper-white);
    font-size: 50px;
    line-height: 1.1;
    letter-spacing: 1px;
  }
  .headline-line {
    position: absolute;
    white-space: nowrap;
    line-height: 1;
    color: var(--headline-yellow);
    -webkit-text-stroke: 14px var(--ink-black);
    paint-order: stroke fill;
    text-shadow:
      0 0 0 var(--paper-white),
      5px 5px 0 var(--paper-white), -5px -5px 0 var(--paper-white),
      5px -5px 0 var(--paper-white), -5px 5px 0 var(--paper-white),
      7px 0 0 var(--paper-white), -7px 0 0 var(--paper-white),
      0 7px 0 var(--paper-white), 0 -7px 0 var(--paper-white);
  }
  .headline-line .particle { font-size: 0.62em; }
  .line-probability { left: 28px; top: 78px; font-size: 172px; letter-spacing: -4px; }
  .line-weekday { left: 28px; top: 222px; font-size: 172px; letter-spacing: -4px; }
  .line-x { left: 300px; top: 350px; font-size: 210px; color: var(--headline-green); }
  .line-reason { left: 330px; top: 515px; font-size: 148px; letter-spacing: -6px; }
  .line-reason .small { font-size: 0.82em; }
</style>
</head>
<body>
  <main class="thumbnail">
    <div class="market-board" role="img" aria-label="株価ボードの写真(緑と赤の数字が並ぶ電光掲示板)"></div>
    <div class="speaker-photo" role="img" aria-label="マイクを持って話すスーツ姿の講師の写真"></div>

    <p class="topic-label">来週の相場は</p>
    <h1 class="headline">
      <span class="headline-line line-probability">高確率<span class="particle">で</span></span>
      <span class="headline-line line-weekday">火曜日<span class="particle">が</span></span>
      <span class="headline-line line-x">X</span>
      <span class="headline-line line-reason">デー<span class="small">の理由</span></span>
    </h1>
  </main>
</body>
</html>
```